Mobile Landing Page for giveaway Seedbombs done from a institution for handicaped people

We are a social institution that makes seedbombs that contain wildflowers for bees and other insects. During a sutanibel event, these bombs are given to an audience. On the packaging of the seedbombs, there is a QR code that leads to a landing page. We are producing a video showing how our handicapped clients made the seebombs. The Landigpage should look: sustanible, green, and sozial. On the page, there shoud be this Video, a manual how tho use the seedbombs. Something about our work whith the handicapt people a linkt to our Instagram amd a possibility to get involved whith us as well as a donation button. You can find more information about us on: www.talmatte-kollektiv.ch

Target Market(s)

People that are intressetet in envirement and social impakt

Industry/Entity Type

Social Impakt, Urban Gardening

Coding

Coded - Design and coding required

Number of Pages Required

1 page

Font styles to use
Other font styles liked:
• Joanna

Requirements
Must have
• Be optimised for smartphone
Nice to have
• like a floating page, witch leads you throug the different steps, mabey like a plant with ist growing. From the Bombs to the Plan. Or a little game ore something.

```html
<!DOCTYPE html>
<html lang="en">
<head>
<meta charset="utf-8">
<title>Talmatte – Seedbomb Landing Page</title>
<link href="https://fonts.googleapis.com/css2?family=Audiowide&family=Nunito+Sans:wght@300;400;600&display=swap" rel="stylesheet">
<style>
:root{
  --canvas:#efeff1;
  --paper:#ffffff;
  --ink:#222222;
  --muted:#555555;
  --terracotta:#c9604d;
  --sage:#b3bea5;
  --sage-dark:#9fae92;
  --sage-soft:#cfd6c6;
  --footer:#f1f2f4;
  --blush:#efe3e1;
  --badge-rose:#f2d3cc;
  --badge-rose-ring:#e7b3a8;
  --badge-green:#b9cbb1;
  --badge-green-ring:#8fa885;
  --badge-blue:#6f809c;
  --badge-blue-ring:#55667f;
  --social:#4a5a78;
  --head:"Audiowide",sans-serif;
  --body:"Nunito Sans",sans-serif;
}
*{box-sizing:border-box;margin:0;padding:0}
html,body{width:677px;height:1200px;overflow:hidden;background:var(--canvas);font-family:var(--body);color:var(--ink)}
.canvas{position:relative;width:677px;height:1200px}
.abs{position:absolute}
.frame{position:absolute;background:var(--paper);box-shadow:0 1px 4px rgba(0,0,0,.08);overflow:hidden}
.desktop{left:25px;top:53px;width:470px;height:1062px}
.mobile{left:527px;top:53px;width:126px;height:960px}

.brand{position:absolute;display:flex;align-items:center;gap:3px;font-family:var(--body);font-weight:600;color:var(--ink);letter-spacing:.06em;white-space:nowrap}
.brand .dot{border-radius:50%;background:var(--sage-dark)}

.nav{position:absolute;font-size:6px;font-weight:400;color:var(--ink);white-space:nowrap}
.nav span{white-space:nowrap}
.heading{position:absolute;font-family:var(--head);color:var(--ink);font-weight:400;white-space:nowrap}
.copy{position:absolute;font-weight:300;color:var(--ink)}
.btn{position:absolute;background:var(--terracotta);color:#fff;font-weight:300;display:flex;align-items:center;justify-content:center;border-radius:2px;white-space:nowrap}
.photo{position:absolute}
.arrow-chip{position:absolute;background:#fff;border:2px solid var(--sage);border-radius:5px;display:flex;align-items:center;justify-content:center}
.welcome{position:absolute;left:0;right:0;text-align:center;font-family:var(--head);color:#fff;white-space:nowrap}
.play{position:absolute;border-radius:50%;background:#fff}
.play::after{content:"";position:absolute;top:50%;left:54%;transform:translate(-50%,-50%);border-style:solid;border-color:transparent transparent transparent var(--ink)}
.desktop .play::after{border-width:5px 0 5px 8px}
.mobile .play::after{border-width:2.5px 0 2.5px 4px}

.involved{position:absolute;background:var(--sage);left:0;right:0}
.footer{position:absolute;background:var(--footer);left:0;right:0}
.strip{position:absolute;left:0;right:0;background:var(--blush)}
.badge{position:absolute;border-radius:50%;border:1.5px solid}
.badge.rose{background:var(--badge-rose);border-color:var(--badge-rose-ring)}
.badge.green{background:var(--badge-green);border-color:var(--badge-green-ring)}
.badge.blue{background:var(--badge-blue);border-color:var(--badge-blue-ring)}
.social{position:absolute;border-radius:50%;background:var(--social)}
.slide-btn{position:absolute;border-radius:50%;background:#fff;border:1px solid var(--sage);display:flex;align-items:center;justify-content:center}
</style>
</head>
<body>
<div class="canvas">

  <!-- Desktop layout -->
  <section class="frame desktop">
    <header>
      <div class="brand" style="left:40px;top:16px;font-size:7px"><span class="dot" style="width:9px;height:9px"></span>TALMATTE</div>
      <nav class="nav" style="left:234px;top:18px">
        <span class="abs" style="left:0">Current</span>
        <span class="abs" style="left:35px">Offer</span>
        <span class="abs" style="left:64px">About Us</span>
        <span class="abs" style="left:101px">Contact</span>
        <span class="abs" style="left:137px">Account</span>
        <span class="abs" style="left:178px">Shop</span>
      </nav>
    </header>

    <div class="hero abs" style="left:0;top:41px;width:470px;height:320px">
      <svg width="470" height="320" viewBox="0 0 470 320" class="abs" style="left:0;top:0">
        <defs>
          <linearGradient id="heroTone" x1="0" y1="0" x2="1" y2="1">
            <stop offset="0" stop-color="#7d7468"/>
            <stop offset=".45" stop-color="#3c4f82"/>
            <stop offset=".75" stop-color="#8a6a4c"/>
            <stop offset="1" stop-color="#b07d4e"/>
          </linearGradient>
          <linearGradient id="waveTone" x1="0" y1="0" x2="0" y2="1">
            <stop offset="0" stop-color="var(--sage-soft)" stop-opacity=".9"/>
            <stop offset="1" stop-color="var(--sage-soft)" stop-opacity=".15"/>
          </linearGradient>
        </defs>
        <path role="img" aria-label="Soft dotted wave texture in sage" d="M0 189C120 215 260 266 348 269C400 270 440 255 470 222V318C420 300 360 262 280 262C200 262 110 262 0 252Z" fill="url(#waveTone)"/>
        <path role="img" aria-label="Video still: clients crafting seedbombs at a workshop table" d="M0 0H470V222C440 255 400 270 348 269C260 266 120 215 0 189Z" fill="url(#heroTone)"/>
        <path d="M0 189C120 215 260 266 348 269C400 270 440 255 470 222" fill="none" stroke="var(--terracotta)" stroke-width="4"/>
      </svg>
      <div class="play" style="left:223px;top:84px;width:23px;height:23px"></div>
      <div class="welcome" style="top:117px;font-size:13px">WELCOME TO</div>
      <div class="welcome" style="top:134px;font-size:24px">TALMATTE</div>
      <div class="arrow-chip" style="left:220px;top:229px;width:31px;height:31px">
        <svg width="12" height="12" viewBox="0 0 12 12"><path d="M6 1V11M2 7L6 11L10 7" fill="none" stroke="var(--sage-dark)" stroke-width="1"/></svg>
      </div>
    </div>

    <h2 class="heading" style="left:44px;top:368px;font-size:10.5px">HOW TO USE</h2>
    <p class="copy" style="left:44px;top:393px;width:180px;font-size:6.5px;line-height:11.4px;text-align:justify">Lorem ipsum dolor sit amet, consectetur adipiscing elit, sed do eiusmod tempor incididunt ut labore et dolore magna aliqua. Quis ipsum suspendisse ultrices gravida. Risus commodo viverra maecenas accumsan lacus vel facilisis. Lorem ipsum dolor sit amet, consectetur adipiscing elit, sed do eiusmod tempor incididunt ut labore et dolore magna aliqua. Quis ipsum suspendisse ultrices gravida.</p>
    <div class="btn" style="left:44px;top:486px;width:56px;height:16px;font-size:7px">Read More</div>
    <div class="photo" role="img" aria-label="Hand holding several round seedbombs" style="left:255px;top:373px;width:174px;height:128px;border:2px solid var(--sage);border-radius:5px;background:linear-gradient(135deg,#8f8a84,#d9c3b6 45%,#6f6258 75%,#b9a79b)"></div>
    <div class="photo" role="img" aria-label="Single seedbomb with soft shadow" style="left:234px;top:450px;width:66px;height:62px;border-radius:50%;background:radial-gradient(circle at 40% 40%,#8b7a6c,#4f4339)"></div>

    <h2 class="heading" style="left:0;right:0;text-align:center;top:570px;font-size:10.5px">OUR WORK</h2>
    <p class="copy" style="left:40px;width:390px;top:598px;font-size:6.5px;line-height:11.4px;text-align:center">Lorem ipsum dolor sit amet, consectetur adipiscing elit, sed do eiusmod tempor incididunt ut labore et dolore magna aliqua. Quis ipsum suspendisse ultrices gravida. Risus commodo viverra maecenas accumsan lacus vel facilisis. Lorem ipsum dolor sit amet, consectetur adipiscing elit, sed do eiusmod tempor incididunt ut labore et dolore magna aliqua.</p>
    <div class="photo" role="img" aria-label="Group of people outdoors in a courtyard" style="left:3px;top:649px;width:111px;height:79px;background:linear-gradient(180deg,#6f8a4e,#9a9c9c 60%,#7b7d82)"></div>
    <div class="photo" role="img" aria-label="Two men at a garden event tent" style="left:121px;top:649px;width:111px;height:79px;background:linear-gradient(180deg,#e8e6e0,#6f8f52 60%,#c4bfa9)"></div>
    <div class="photo" role="img" aria-label="Workshop with clients making seedbombs" style="left:238px;top:649px;width:111px;height:79px;background:linear-gradient(135deg,#7d7468,#3c4f82 55%,#b07d4e)"></div>
    <div class="photo" role="img" aria-label="Residents laughing together indoors" style="left:355px;top:649px;width:111px;height:79px;background:linear-gradient(135deg,#9aa0a8,#b9443e 50%,#cfd5de)"></div>
    <div class="slide-btn" style="left:0;top:681px;width:14px;height:14px"><svg width="7" height="7" viewBox="0 0 8 8"><path d="M7 4H1M3.5 1.5L1 4L3.5 6.5" fill="none" stroke="var(--sage-dark)" stroke-width=".8"/></svg></div>
    <div class="slide-btn" style="left:456px;top:681px;width:14px;height:14px"><svg width="7" height="7" viewBox="0 0 8 8"><path d="M1 4H7M4.5 1.5L7 4L4.5 6.5" fill="none" stroke="var(--sage-dark)" stroke-width=".8"/></svg></div>
    <div class="btn" style="left:207px;top:745px;width:56px;height:17px;font-size:7px">Learn More</div>

    <section class="involved" style="top:800px;height:121px">
      <h2 class="heading" style="left:0;right:0;text-align:center;top:23px;font-size:10.5px">GET INVOLVED</h2>
      <p class="copy" style="left:40px;width:390px;top:49px;font-size:6.5px;line-height:11.4px;text-align:center">Lorem ipsum dolor sit amet, consectetur adipiscing elit, sed do eiusmod tempor incididunt ut labore et dolore magna aliqua. Quis ipsum suspendisse ultrices gravida. Risus commodo viverra maecenas accumsan lacus vel facilisis.</p>
      <div class="btn" style="left:207px;top:83px;width:56px;height:17px;font-size:7px">Donate Now</div>
    </section>

    <footer class="footer" style="top:921px;height:141px">
      <div class="brand" style="left:40px;top:52px;font-size:10px"><span class="dot" style="width:12px;height:12px"></span>TALMATTE</div>
      <div class="badge rose" style="left:318px;top:40px;width:31px;height:31px"></div>
      <div class="badge green" style="left:355px;top:40px;width:31px;height:31px"></div>
      <div class="badge blue" style="left:392px;top:40px;width:31px;height:31px"></div>
      <div class="strip" style="top:88px;height:20px">
        <nav class="nav" style="left:44px;top:6px;font-size:7px">
          <span class="abs" style="left:0">Current</span>
          <span class="abs" style="left:42px">Offer</span>
          <span class="abs" style="left:76px">About Us</span>
          <span class="abs" style="left:123px">Contact Account</span>
          <span class="abs" style="left:193px">Shop</span>
        </nav>
        <span class="social" style="left:370px;top:5px;width:10px;height:10px"></span>
        <span class="social" style="left:385px;top:5px;width:10px;height:10px"></span>
        <span class="social" style="left:399px;top:5px;width:10px;height:10px"></span>
        <span class="social" style="left:413px;top:5px;width:10px;height:10px"></span>
      </div>
      <p class="copy" style="left:0;right:0;top:121px;font-size:6px;text-align:center;font-weight:400;color:var(--muted)">© Copyrights 2023 talmatte | All Rights Reserved</p>
    </footer>
  </section>

  <!-- Mobile layout -->
  <section class="frame mobile">
    <svg class="abs" style="left:9px;top:13px" width="7" height="6" viewBox="0 0 7 6"><path d="M0 .5H7M0 3H7M0 5.5H7" stroke="var(--ink)" stroke-width="1"/></svg>
    <div class="brand" style="left:42px;top:12px;font-size:5px"><span class="dot" style="width:6px;height:6px"></span>TALMATTE</div>

    <div class="hero abs" style="left:0;top:31px;width:126px;height:160px">
      <svg width="126" height="160" viewBox="0 0 126 160" class="abs" style="left:0;top:0">
        <defs>
          <linearGradient id="heroToneM" x1="0" y1="0" x2="1" y2="1">
            <stop offset="0" stop-color="#8a7a64"/>
            <stop offset=".5" stop-color="#3c4f82"/>
            <stop offset="1" stop-color="#a67a4e"/>
          </linearGradient>
          <linearGradient id="waveToneM" x1="0" y1="0" x2="0" y2="1">
            <stop offset="0" stop-color="var(--sage-soft)" stop-opacity=".9"/>
            <stop offset="1" stop-color="var(--sage-soft)" stop-opacity=".15"/>
          </linearGradient>
        </defs>
        <path role="img" aria-label="Soft dotted wave texture in sage" d="M0 107C20 115 40 122 63 123C90 124 110 120 126 111V156C100 148 80 140 55 140C35 140 15 143 0 142Z" fill="url(#waveToneM)"/>
        <path role="img" aria-label="Video still: client crafting seedbombs" d="M0 0H126V111C110 120 90 124 63 123C40 122 20 115 0 107Z" fill="url(#heroToneM)"/>
        <path d="M0 107C20 115 40 122 63 123C90 124 110 120 126 111" fill="none" stroke="var(--terracotta)" stroke-width="1.5"/>
      </svg>
      <div class="play" style="left:58px;top:41px;width:10px;height:10px"></div>
      <div class="welcome" style="top:57px;font-size:7px">WELCOME TO</div>
      <div class="welcome" style="top:67px;font-size:12px">TALMATTE</div>
      <div class="arrow-chip" style="left:56px;top:112px;width:14px;height:14px;border-width:1px;border-radius:3px">
        <svg width="6" height="6" viewBox="0 0 12 12"><path d="M6 1V11M2 7L6 11L10 7" fill="none" stroke="var(--sage-dark)" stroke-width="1.5"/></svg>
      </div>
    </div>

    <div class="photo" role="img" aria-label="Hand holding several round seedbombs" style="left:20px;top:185px;width:95px;height:70px;border:1.5px solid var(--sage);border-radius:4px;background:linear-gradient(135deg,#8f8a84,#d9c3b6 45%,#6f6258 75%,#b9a79b)"></div>
    <div class="photo" role="img" aria-label="Single seedbomb" style="left:9px;top:226px;width:36px;height:34px;border-radius:50%;background:radial-gradient(circle at 40% 40%,#8b7a6c,#4f4339)"></div>

    <h2 class="heading" style="left:8px;top:284px;font-size:8px">HOW TO USE</h2>
    <p class="copy" style="left:8px;top:304px;width:111px;font-size:5px;line-height:9.3px;text-align:justify">Lorem ipsum dolor sit amet, consectetur adipiscing elit, sed do eiusmod tempor incididunt ut labore et dolore magna aliqua. Quis ipsum suspendisse ultrices gravida. Risus commodo viverra maecenas accumsan lacus vel facilisis. Lorem ipsum dolor sit amet, consectetur adipiscing elit, sed do eiusmod tempor incididunt ut labore et dolore magna aliqua.</p>
    <div class="btn" style="left:8px;top:401px;width:38px;height:12px;font-size:5px">Read More</div>

    <h2 class="heading" style="left:8px;top:448px;font-size:8px">OUR WORK</h2>
    <p class="copy" style="left:8px;top:467px;width:111px;font-size:5px;line-height:9.3px;text-align:justify">Lorem ipsum dolor sit amet, consectetur adipiscing elit, sed do eiusmod tempor incididunt ut labore et dolore magna aliqua. Quis ipsum suspendisse ultrices gravida.</p>
    <div class="photo" role="img" aria-label="Group of people outdoors in a courtyard" style="left:6px;top:519px;width:98px;height:69px;background:linear-gradient(180deg,#6f8a4e,#9a9c9c 60%,#7b7d82)"></div>
    <div class="photo" role="img" aria-label="Garden event scene" style="left:109px;top:519px;width:17px;height:69px;background:linear-gradient(180deg,#e8e6e0,#6f8f52)"></div>
    <div class="slide-btn" style="left:0;top:549px;width:8px;height:8px"></div>
    <div class="slide-btn" style="left:118px;top:549px;width:8px;height:8px"></div>
    <div class="btn" style="left:8px;top:601px;width:38px;height:12px;font-size:5px">Learn More</div>

    <section class="involved" style="top:647px;height:126px">
      <h2 class="heading" style="left:0;right:0;text-align:center;top:25px;font-size:7.5px">GET INVOLVED</h2>
      <p class="copy" style="left:10px;width:106px;top:44px;font-size:5px;line-height:9.3px;text-align:center">Lorem ipsum dolor sit amet, consectetur adipiscing elit, sed do eiusmod tempor incididunt ut labore et dolore magna aliqua. Quis ipsum suspendisse ultrices gravida.</p>
      <div class="btn" style="left:43px;top:94px;width:38px;height:12px;font-size:5px">Donate Now</div>
    </section>

    <footer class="footer" style="top:773px;height:187px">
      <div class="brand" style="left:26px;top:38px;font-size:8px"><span class="dot" style="width:10px;height:10px"></span>TALMATTE</div>
      <div class="badge rose" style="left:19px;top:77px;width:26px;height:26px"></div>
      <div class="badge green" style="left:50px;top:77px;width:26px;height:26px"></div>
      <div class="badge blue" style="left:81px;top:77px;width:26px;height:26px"></div>
      <div class="strip" style="top:119px;height:35px">
        <p class="copy" style="left:0;right:0;top:6px;text-align:center;font-size:4.3px;font-weight:400;white-space:nowrap">Current | Offer | About Us | Contact Account | Shop</p>
        <span class="social" style="left:42px;top:19px;width:8px;height:8px"></span>
        <span class="social" style="left:53px;top:19px;width:8px;height:8px"></span>
        <span class="social" style="left:64px;top:19px;width:8px;height:8px"></span>
        <span class="social" style="left:75px;top:19px;width:8px;height:8px"></span>
      </div>
      <p class="copy" style="left:0;right:0;top:168px;font-size:4.3px;text-align:center;font-weight:400;color:var(--muted);white-space:nowrap">© Copyrights 2023 talmatte | All Rights Reserved</p>
    </footer>
  </section>

</div>
</body>
</html>
```